Musician looking for catchy Web Design for promotion

My name is Brenna Colfer. I'm an Irish musician who plays the tin whistle and the flute. I'm also the leader of a traditional Irish music and dance ensemble called Wander the Hillside (www.wanderthehillside-example.com) and for the past 30 years, I've toured the world performing thousands of concerts. I run an annual cruise (www.brennacolfervoyage-example.com) that I would like a link to, and I'm also I'm organizing tours to Ireland that I would like a page set up for. I'm looking for a website to promote my tours and my music.
Updates

Hello Graphic Designers, I am only looking for the design of the home page to make my decision. Thank you. Brenna

Target Market(s)

Music fans of Irlsh and World Music

Industry/Entity Type

Entertainment Industry

Number of Pages Required

5+ page

Requirements
Must have
• I'm looking for a catchy design that shows a photo of me. I would like a few links....
• BIO
• TOURDATES
• BRENNA COLFER CRUISE
• MUSICAL TOUR OF IRELAND
• CONTACT
• VIDEO
• GALLERY
• CONTACT
• MAILING LIST
• STORE
Nice to have
• we'll see!

```html
<!DOCTYPE html>
<html lang="en">
<head>
<meta charset="utf-8">
<title>Brenna Colfer – Musical Tour of Ireland</title>
<link href="https://fonts.googleapis.com/css2?family=Roboto:wght@300;400;500&family=Marcellus&display=swap" rel="stylesheet">
<style>
:root{
  --navy:#0b3b75;
  --navy-dark:#082f60;
  --footer:#0d3f7c;
  --footer-bottom:#0a3468;
  --blue:#1d5ea6;
  --green:#5aa832;
  --page:#f4f4f4;
  --ink:#2b2b2b;
  --muted:#6b6b6b;
  --white:#ffffff;
}
*{margin:0;padding:0;box-sizing:border-box}
html,body{width:1200px;height:2228px;overflow:hidden}
body{position:relative;background:var(--page);font-family:'Roboto',sans-serif;color:var(--ink)}
.abs{position:absolute}
a{color:inherit;text-decoration:none}

/* header */
.header-band{left:0;top:0;width:1200px;height:172px;background:var(--navy)}
.rays{left:0;top:172px;width:1200px;height:583px;background:radial-gradient(ellipse at 50% 30%,#ffffff 0%,#e9e9e9 45%,#cfcfcf 100%)}
.main-nav{left:74px;top:12px;width:1052px;height:50px;border-top:3px solid #0e4a8c;display:flex;justify-content:space-between;align-items:center;padding:0 20px;font-size:14.5px;color:var(--white)}
.main-nav a.active{color:#7dd04f;position:relative}
.main-nav a.active::before{content:"";position:absolute;left:-14px;right:-14px;top:-17px;height:4px;background:var(--green)}
.logo-box{left:74px;top:64px;width:1052px;height:108px;background:var(--white);display:flex;align-items:center;justify-content:center;gap:12px}
.logo-mark{width:26px;height:26px;border-radius:50%;background:#222}
.logo-text{font-size:14px;font-weight:500;color:#222;line-height:1.2;letter-spacing:.5px}

.slider{left:74px;top:181px;width:1052px;height:449px;background:linear-gradient(180deg,#0b0b0b 0%,#0b0b0b 18%,#c9a868 22%,#8a1f12 45%,#a7321d 75%,#6e170d 100%)}
.slider-edge{left:74px;top:630px;width:1052px;height:6px;background:var(--white)}
.dots{left:576px;top:596px;display:flex;gap:6px}
.dots span{width:11px;height:11px;border-radius:50%;background:var(--white)}
.dots span.on{background:var(--green)}

/* welcome */
.welcome{left:74px;top:680px;width:1052px;height:217px;background:var(--white);text-align:center;box-shadow:0 14px 16px -12px rgba(0,0,0,.28)}
.welcome h1{font-weight:400;font-size:30px;margin-top:32px;letter-spacing:.5px}
.welcome h1 em{font-style:normal;color:var(--green)}
.welcome p{font-size:14px;line-height:25px;color:var(--muted);width:990px;margin:14px auto 0}
.read-more{display:flex;align-items:center;justify-content:center;gap:10px;color:var(--green);font-size:14px;font-weight:500}
.welcome .read-more{margin-top:14px}

/* work */
.work-title{left:0;top:948px;width:1200px;text-align:center;font-size:30px;font-weight:400}
.work-sub{left:0;top:986px;width:1200px;text-align:center;font-size:14px;color:var(--muted)}
.work{left:74px;top:1025px;width:1052px;display:flex;justify-content:space-between}
.work-card{width:242px;height:166px;background:var(--white);padding:7px;box-shadow:0 1px 4px rgba(0,0,0,.12);position:relative}
.work-card.featured{box-shadow:0 2px 10px rgba(0,0,0,.35)}
.work-img{width:100%;height:100%}
.work-caption{position:absolute;left:7px;right:7px;bottom:7px;height:44px;background:rgba(0,0,0,.55);color:var(--white);font-size:15px;padding:14px 14px 0}

/* columns */
.cols{left:74px;top:1244px;width:1052px;display:flex;justify-content:space-between}
.col{width:332px;height:496px;background:var(--white);border-top:6px solid var(--blue);position:relative;text-align:center}
.col.green{border-top-color:var(--green)}
.col h2{font-weight:400;font-size:27px;color:#0e3c78;margin-top:35px}
.col.green h2{color:var(--green)}
.col hr{border:0;border-top:1px solid #e3e3e3;margin:18px 18px 0}
.about-photo{width:270px;height:149px;margin:12px auto 0;background:linear-gradient(135deg,#3b3a36,#6b5a4a 55%,#2a2824)}
.about-lead{font-size:14.5px;line-height:22px;color:var(--blue);width:296px;margin:20px auto 0}
.about-text{font-size:13.5px;line-height:22px;color:#444;width:296px;margin:18px auto 0}
.col .read-more{margin-top:18px}
.flourish{width:130px;height:26px;margin:8px auto 0;background:#f2f6f0}
.video{width:298px;height:228px;margin:12px auto 0;background:linear-gradient(135deg,#2a1a14,#7a4a3a 50%,#3b2a24);position:relative}
.play{position:absolute;left:121px;top:86px}
.video-text{font-size:13.5px;line-height:22px;color:#444;width:296px;margin:20px auto 0;text-align:justify;text-align-last:center}
.col-bar{position:absolute;left:0;right:0;bottom:0;height:38px;background:var(--green);color:var(--white);font-size:13.5px;text-align:right;padding:10px 22px 0}
.col-bar.blue{background:var(--blue)}
.news{text-align:left;padding:0 18px}
.news-date{font-family:'Marcellus',serif;font-size:44px;color:#6a7fa3;margin-top:22px;line-height:1}
.news-text{font-size:13.5px;line-height:22px;color:#444;margin-top:14px;text-align:justify}
.news-sep{border-top:1px dotted #cfcfcf;margin-top:26px}

/* banner */
.banner{left:74px;top:1788px;width:1052px;height:105px;background:linear-gradient(90deg,#3a2414,#5a3a1e 45%,#7a5226 75%,#3a2414)}
.banner-frame{left:86px;top:1800px;width:1030px;height:81px;border:1px solid rgba(255,255,255,.45)}
.banner-title{left:117px;top:1814px;font-size:22px;color:var(--white)}
.banner-text{left:117px;top:1845px;font-size:14.5px;color:#e6e6e6}
.book-btn{left:901px;top:1822px;width:183px;height:39px;background:#5cc13a;color:var(--white);font-size:16px;font-weight:500;text-align:center;line-height:39px;border-radius:2px}

/* footer */
.footer{left:0;top:1942px;width:1200px;height:223px;background:var(--footer)}
.footer-bottom{left:0;top:2165px;width:1200px;height:63px;background:var(--footer-bottom)}
.f-head{top:1982px;font-size:19px;color:var(--white)}
.f-links{top:2020px;list-style:none;font-size:12.5px;color:var(--white)}
.f-links li{height:28px}
.f-links li::before{content:"»";margin-right:7px}
.f-note{left:614px;top:2020px;font-size:13px;line-height:21px;color:var(--white)}
.f-input{left:614px;top:2079px;width:227px;height:31px;background:#0a3366;border:1px solid #194d8d;color:#8aa0c2;font-size:12.5px;padding:8px 14px}
.f-input span{position:absolute;right:12px;top:6px;color:#8aa0c2}
.contact{left:895px;top:2020px;font-size:13px;line-height:28px;color:var(--white)}
.contact div{display:flex;align-items:center;gap:8px}
.copyright{left:74px;top:2189px;font-size:12.5px;color:var(--white)}
.social{left:1014px;top:2182px;display:flex;gap:10px}
.social span{width:30px;height:30px;border:2px solid var(--white);border-radius:50%}
</style>
</head>
<body>

<div class="abs header-band"></div>
<div class="abs rays" role="img" aria-label="Soft grey radiating light backdrop"></div>

<nav class="abs main-nav">
  <a class="active" href="#">Home</a><a href="#">Bio</a><a href="#">Tourdates</a><a href="#">Brenna Colfer Cruise</a><a href="#">Musical Tour Of Ireland</a><a href="#">Contact</a><a href="#">Video</a><a href="#">Gallery</a><a href="#">Contact</a><a href="#">Mailing List</a><a href="#">Store</a>
</nav>

<div class="abs logo-box">
  <span class="logo-mark"></span>
  <div class="logo-text">BRENNA COLFER'S<br>MUSICAL TOUR OF IRELAND</div>
</div>

<div class="abs slider" role="img" aria-label="Photo of tin whistles and flutes lined up in a red and gold instrument roll"></div>
<div class="abs slider-edge"></div>
<div class="abs dots"><span class="on"></span><span></span><span></span></div>

<section class="abs welcome">
  <h1>WELCOME TO OUR <em>SITE</em></h1>
  <p>Beciegast nveriti vitaesaert asety kertya aset aplica boserde nerafae kertyurauestyasnemo faseran. Ptaiadeser daesraed sdrasrolern atur aut oditaut. onsequserantur magni dolqui ratione voluptatemsequi nesciunt Beciegast nveriti vitaesaert asety kertya aset aplica boserde nerafae kertyurauestyasnemo faseran. Ptaiadeser daesraed sdrasrolern atur..</p>
  <div class="read-more">
    <svg width="26" height="8" viewBox="0 0 26 8"><path d="M1 5 Q7 0 13 4 T25 3" fill="none" stroke="#5aa832" stroke-width="1.3"/></svg>
    READ MORE
    <svg width="26" height="8" viewBox="0 0 26 8"><path d="M1 3 Q7 8 13 4 T25 5" fill="none" stroke="#5aa832" stroke-width="1.3"/></svg>
  </div>
</section>

<h2 class="abs work-title">OUR WORK</h2>
<p class="abs work-sub">Beciegast nveriti vitaesaert asety kertya aset aplica boserde nerafae kertyurauesty</p>
<div class="abs work">
  <div class="work-card featured">
    <div class="work-img" role="img" aria-label="Photo of a musician playing the fiddle" style="background:linear-gradient(135deg,#1d1410,#6a3a1c 50%,#2a1a10)"></div>
    <div class="work-caption">THE COMPLETE ANGLER</div>
  </div>
  <div class="work-card"><div class="work-img" role="img" aria-label="Photo of a bodhrán drum and fiddle" style="background:linear-gradient(135deg,#2a2a2a,#8a7a60 50%,#1e1e1e)"></div></div>
  <div class="work-card"><div class="work-img" role="img" aria-label="Photo of hands playing a carved wooden flute" style="background:linear-gradient(135deg,#2a2a6a,#b06a5a 50%,#5a2a6a)"></div></div>
  <div class="work-card"><div class="work-img" role="img" aria-label="Black and white photo of a flute player" style="background:linear-gradient(135deg,#0c0c0c,#3a3a3a 55%,#0c0c0c)"></div></div>
</div>

<div class="abs cols">
  <section class="col">
    <h2>ABOUT US</h2>
    <hr>
    <div class="about-photo" role="img" aria-label="Portrait photo of Brenna Colfer beside an iron gate"></div>
    <p class="about-lead">BRENNA COLFER is considered one of the greatest musicians and personalities in the history of Irish music in America.</p>
    <p class="about-text">She was born in the Bronx, New York of Irish parents, and she is the second oldest of seven children raised in a musical.</p>
    <div class="read-more">
      <svg width="26" height="8" viewBox="0 0 26 8"><path d="M1 5 Q7 0 13 4 T25 3" fill="none" stroke="#5aa832" stroke-width="1.3"/></svg>
      READ MORE
      <svg width="26" height="8" viewBox="0 0 26 8"><path d="M1 3 Q7 8 13 4 T25 5" fill="none" stroke="#5aa832" stroke-width="1.3"/></svg>
    </div>
  </section>

  <section class="col green">
    <h2>VIDEO'S</h2>
    <div class="flourish" role="img" aria-label="Decorative scroll flourish"></div>
    <div class="video" role="img" aria-label="Video still of hands playing a flute">
      <svg class="play" width="56" height="56" viewBox="0 0 56 56"><circle cx="28" cy="28" r="27" fill="#fff"/><path d="M22 16 L40 28 L22 40 Z" fill="#111"/></svg>
    </div>
    <p class="video-text">Nasriosa measisi ut aliquid ex eade consequatur. Nasasuis autem velreprend eriui csn ea voluptate velit</p>
    <a class="col-bar" href="#">› view more video's</a>
  </section>

  <section class="col">
    <h2>LATEST NEW'S</h2>
    <hr>
    <div class="news">
      <div class="news-date">14.05</div>
      <p class="news-text">Nasectetur, adipisci velit, sed quiamiuytasa dolore agnam aliquam quaerat vuptatem nitrase nimad minima veniscipit.</p>
      <div class="news-sep"></div>
      <div class="news-date">12.05</div>
      <p class="news-text">Nasectetur, adipisci velit, sed quiamiuytasa dolore agnam aliquam quaerat vuptatem nitrase nimad minima veniscipit.</p>
    </div>
    <a class="col-bar blue" href="#">› read more news</a>
  </section>
</div>

<div class="abs banner" role="img" aria-label="Warm brown photo of a vintage tour poster"></div>
<div class="abs banner-frame"></div>
<div class="abs banner-title">IRISH MUSIC IN AMERICA</div>
<div class="abs banner-text">Nasriosa measisi ut aliquid ex eade consequatur. Nasasuis autem velreprend eriui csn ea voluptate velit</div>
<a class="abs book-btn" href="#">BOOK US NOW</a>

<footer>
  <div class="abs footer"></div>
  <div class="abs footer-bottom"></div>
  <h3 class="abs f-head" style="left:74px">NAVIGATION</h3>
  <ul class="abs f-links" style="left:74px"><li>Company Info</li><li>Company Blog</li><li>Opportunities</li><li>Email Login</li></ul>
  <ul class="abs f-links" style="left:245px"><li>Site Map</li><li>Publications</li><li>News</li><li>Terms of Use</li></ul>
  <ul class="abs f-links" style="left:408px"><li>Privacy Policy</li><li>Return Policy</li><li>Security Policy</li><li>Help Desk</li></ul>
  <h3 class="abs f-head" style="left:614px">NEWSLETTER</h3>
  <p class="abs f-note">Sign Up for our Newsletter<br>E-mail Address</p>
  <div class="abs f-input">Email*<span>›</span></div>
  <h3 class="abs f-head" style="left:895px">CONTACT INFO</h3>
  <div class="abs contact">
    <div>482 Larkspur Ave. Millbrook, WI 53901</div>
    <div><svg width="12" height="12" viewBox="0 0 24 24"><path fill="#fff" d="M6.6 10.8a15 15 0 006.6 6.6l2.2-2.2a1 1 0 011-.25 11.4 11.4 0 003.6.57 1 1 0 011 1V20a1 1 0 01-1 1A17 17 0 013 4a1 1 0 011-1h3.5a1 1 0 011 1c0 1.25.2 2.45.57 3.57a1 1 0 01-.25 1z"/></svg>Phone: (555) 014-2231</div>
    <div><svg width="12" height="12" viewBox="0 0 24 24"><path fill="#fff" d="M5 2h10v5H5zM3 8h18v10h-3v4H6v-4H3zm5 7v5h8v-5z"/></svg>Fax: (555) 014-2239</div>
  </div>
  <div class="abs copyright">(c) 2016 Brenna Colfer. All Right Reserved.</div>
  <div class="abs social" aria-label="Social links"><span></span><span></span><span></span></div>
</footer>

</body>
</html>
```